Australian Legal Practice would like a Web Design

I need a web design for a newly established law practice operating as Brindell Legal.

I would like the business to have an internet presence (via a website) essentially for the purpose of marketing and advertising. As the business grows (hopefully) I may be interested in providing general legal information as a means of establishing goodwill in the community and a easy and user friends contact method through the website.

The essence of the business is personal legal service based on local knowledge and therefore i want the website to present a picture of friendly professionalism, but mostly i want people who to be able to find the contact details of the business

I would like to have a map of the office location, and photos of the front of the office, the staff (me at the moment) and picture of law themed items and featuring the Brindell Legal logo.

The areas of law which Brindell Legal practises in are as follows:

commercial law
business sale and purchases
leases
conveyancing and property law
wills and estates
powers of attorney
general legal advice
succession planning
Updates

Target Market(s)

Potential and existing clients of the firm
Other law firms
Associated stakeholders, i.e. Banks and real estate agents

Industry/Entity Type

Law Firm

Coding

Coded - Design and coding required

Number of Pages Required

2 page

Font styles to use
Sans Serif

Colors
85acd3
33a6d7
0456a4

Requirements
Must have
• Brindell Legal logo
• Map of the office location
• Picture of Ross Kedwick (principal solicitor)
• Picture of the office
• Areas of Practice
• Address of office
• email address: ross.kedwick@brindelllegal-example.com.au
• Physical address: 17 Pellow Road, Hamilton VIC 3300
• Phone number: (03) 5598 4731
• Facsimile number: (03) 5598 4706
• Space for a brief description of the firm and its competitive advantage
• Bar Guild Logo
• Links to the Bar Guild of Victoria
• Link to the practitioner oversight Council
Nice to have
• coded to wordpress format

```html
<!DOCTYPE html>
<html lang="en">
<head>
<meta charset="utf-8">
<title>Brindell Legal</title>
<link href="https://fonts.googleapis.com/css2?family=Open+Sans:wght@400;600;700&display=swap" rel="stylesheet">
<style>
:root{
  --royal:#0b3da6;
  --royal-dark:#08318c;
  --sky:#33a6d7;
  --steel:#85acd3;
  --ink:#2b2b2b;
  --muted:#6b6b6b;
  --rule:#d9d9d9;
  --paper:#ffffff;
  --mist:#f1f1f1;
  --wood:#5a3a24;
  --wood-dark:#2a1a10;
  --wood-light:#9a6a43;
}
*{box-sizing:border-box;margin:0;padding:0}
html,body{width:1200px;height:2284px;overflow:hidden}
body{font-family:"Open Sans",Arial,sans-serif;color:var(--ink);background:var(--paper);font-size:13px;line-height:1.55}
a{color:inherit;text-decoration:none}

.site-header{height:68px;border-top:4px solid var(--royal);position:relative;background:var(--paper)}
.brand{position:absolute;left:160px;top:12px;display:flex;align-items:center;gap:10px}
.brand-mark{width:14px;height:14px;background:var(--royal)}
.brand-name{font-size:26px;font-weight:700;color:var(--royal);letter-spacing:.5px}
.header-phone{position:absolute;right:160px;top:6px;font-size:12px;color:var(--ink);display:flex;align-items:center;gap:6px}
.main-nav{position:absolute;right:160px;top:32px;display:flex;gap:4px}
.main-nav a{font-size:11.5px;padding:4px 10px;color:var(--ink)}
.main-nav a.is-current{background:var(--royal);color:#fff;border-radius:2px}

.hero{height:472px;background:radial-gradient(ellipse at 55% 55%,var(--wood-light) 0%,var(--wood) 40%,var(--wood-dark) 100%)}

.welcome{height:220px;text-align:center;padding-top:28px}
.welcome h1{font-size:22px;font-weight:600;color:var(--royal)}
.welcome .rule{width:880px;height:1px;background:var(--rule);margin:12px auto 14px;position:relative}
.welcome .rule::after{content:"";position:absolute;left:50%;top:-1px;width:80px;height:3px;margin-left:-40px;background:var(--royal)}
.welcome p{width:880px;margin:0 auto;font-size:12.5px;color:var(--ink)}

.practice-band{height:840px;background:linear-gradient(180deg,#3b2a1f 0%,#6b4a30 45%,#4a3222 100%);position:relative}
.feature-cards{position:absolute;left:160px;top:32px;display:flex;gap:20px}
.feature-card{width:430px;height:240px;position:relative;overflow:hidden}
.feature-card .photo{position:absolute;inset:0}
.feature-card:first-child .photo{background:linear-gradient(135deg,#8a6a4c,#3a2618)}
.feature-card:last-child .photo{background:linear-gradient(135deg,#3c3c46,#b9a08a)}
.feature-card .caption{position:absolute;left:0;right:0;bottom:0;padding:14px 18px;background:rgba(0,0,0,.45);color:#fff}
.feature-card h3{font-size:14px;font-weight:600}
.feature-card p{font-size:11.5px}

.practice-boxes{position:absolute;left:212px;top:288px;display:flex;gap:20px}
.practice-box{width:380px;background:var(--paper);height:288px}
.practice-box h2{background:var(--royal);color:#fff;text-align:center;font-size:17px;font-weight:600;padding:10px 0;letter-spacing:.5px}
.practice-box ul{list-style:none;padding:12px 22px}
.practice-box li{display:flex;align-items:flex-start;gap:12px;font-size:11.5px;padding:5px 0;border-bottom:1px solid #eee}
.practice-box li:last-child{border-bottom:0}
.practice-box svg{flex:none;margin-top:1px}
.practice-box.law li{padding-left:70px}

.band-intro{position:absolute;left:160px;right:160px;top:620px;text-align:center;color:#fff}
.band-intro h2{font-size:22px;font-weight:600;letter-spacing:1px}
.band-intro p{font-size:12px;margin-top:8px;width:800px;margin-left:auto;margin-right:auto}

.team{height:400px;text-align:center;padding-top:36px}
.team h2{font-size:20px;font-weight:600;color:var(--royal)}
.team-grid{display:flex;justify-content:center;gap:84px;margin-top:32px}
.team-member{width:180px}
.team-member .portrait{height:160px}
.team-member:nth-child(1) .portrait{background:linear-gradient(160deg,#7c5a3c,#2e2018)}
.team-member:nth-child(2) .portrait{background:linear-gradient(160deg,#6e4b2c,#b08a60)}
.team-member:nth-child(3) .portrait{background:linear-gradient(160deg,#8e6d4e,#3a2a20)}
.team-member:nth-child(4) .portrait{background:linear-gradient(160deg,#c7b9a6,#4b3a2e)}
.team-member .name{background:var(--mist);font-size:11.5px;padding:8px 0;color:var(--muted)}

.site-footer{height:284px;background:var(--royal);color:#fff;text-align:center;padding-top:58px}
.footer-nav{display:flex;justify-content:center;gap:22px;font-size:11px}
.social{display:flex;justify-content:center;gap:12px;margin-top:22px}
.social span{width:24px;height:24px;border-radius:50%;background:var(--sky)}
.contact{margin-top:18px;font-size:11.5px;line-height:1.7}
.footer-rule{width:560px;height:1px;background:rgba(255,255,255,.35);margin:16px auto 10px}
.copyright{font-size:11px;color:var(--steel)}
</style>
</head>
<body>

<header class="site-header">
  <a class="brand" href="#"><span class="brand-mark"></span><span class="brand-name">Brindell Legal</span></a>
  <div class="header-phone">
    <svg width="12" height="12" viewBox="0 0 24 24"><path fill="#0b3da6" d="M6.6 10.8a15.1 15.1 0 0 0 6.6 6.6l2.2-2.2c.3-.3.7-.4 1-.2 1.1.4 2.3.6 3.6.6.6 0 1 .4 1 1V20c0 .6-.4 1-1 1A17 17 0 0 1 3 4c0-.6.4-1 1-1h3.5c.6 0 1 .4 1 1 0 1.3.2 2.5.6 3.6.1.3 0 .7-.2 1z"/></svg>
    (03) 5598 4731
  </div>
  <nav class="main-nav">
    <a class="is-current" href="#">Home</a>
    <a href="#">About Us</a>
    <a href="#">Leases</a>
    <a href="#">Estate Planning</a>
    <a href="#">Real Estate</a>
    <a href="#">Legal Services</a>
    <a href="#">Your Contact</a>
  </nav>
</header>

<section class="hero" role="img" aria-label="Wooden judge's gavel resting on its block on a desk"></section>

<section class="welcome">
  <h1>Welcome to Our Site</h1>
  <div class="rule"></div>
  <p>We are a local Hamilton practice offering personal legal service built on local knowledge, clear advice and fair fees for families, farmers and small businesses.</p>
  <p>From buying your first home to planning the future of a family business, we guide you through each step in plain language.</p>
  <p>Call in, phone or email and we will arrange a time that suits you.</p>
</section>

<section class="practice-band" role="group" aria-label="Law office background with books and gavel">
  <div class="feature-cards">
    <article class="feature-card">
      <div class="photo" role="img" aria-label="Law books and scales of justice on a desk"></div>
      <div class="caption"><h3>Our Office</h3><p>Visit us on Pellow Road in the heart of Hamilton, with easy parking and a friendly welcome for every client.</p></div>
    </article>
    <article class="feature-card">
      <div class="photo" role="img" aria-label="Solicitor reviewing documents with a client"></div>
      <div class="caption"><h3>Our Approach</h3><p>Practical advice from a solicitor who knows the district and takes time to listen before acting.</p></div>
    </article>
  </div>

  <div class="practice-boxes">
    <div class="practice-box law">
      <h2>AREAS OF LAW</h2>
      <ul>
        <li><svg width="14" height="14" viewBox="0 0 14 14"><circle cx="7" cy="7" r="6" fill="#33a6d7"/><path d="M4 7.2l2 2 4-4" stroke="#fff" stroke-width="1.6" fill="none"/></svg>Commercial Law</li>
        <li><svg width="14" height="14" viewBox="0 0 14 14"><circle cx="7" cy="7" r="6" fill="#33a6d7"/><path d="M4 7.2l2 2 4-4" stroke="#fff" stroke-width="1.6" fill="none"/></svg>Business Sale and Purchases</li>
        <li><svg width="14" height="14" viewBox="0 0 14 14"><circle cx="7" cy="7" r="6" fill="#33a6d7"/><path d="M4 7.2l2 2 4-4" stroke="#fff" stroke-width="1.6" fill="none"/></svg>Leases</li>
        <li><svg width="14" height="14" viewBox="0 0 14 14"><circle cx="7" cy="7" r="6" fill="#33a6d7"/><path d="M4 7.2l2 2 4-4" stroke="#fff" stroke-width="1.6" fill="none"/></svg>Conveyancing and Property Law</li>
        <li><svg width="14" height="14" viewBox="0 0 14 14"><circle cx="7" cy="7" r="6" fill="#33a6d7"/><path d="M4 7.2l2 2 4-4" stroke="#fff" stroke-width="1.6" fill="none"/></svg>Wills and Estates</li>
        <li><svg width="14" height="14" viewBox="0 0 14 14"><circle cx="7" cy="7" r="6" fill="#33a6d7"/><path d="M4 7.2l2 2 4-4" stroke="#fff" stroke-width="1.6" fill="none"/></svg>Powers of Attorney</li>
        <li><svg width="14" height="14" viewBox="0 0 14 14"><circle cx="7" cy="7" r="6" fill="#33a6d7"/><path d="M4 7.2l2 2 4-4" stroke="#fff" stroke-width="1.6" fill="none"/></svg>General Legal Advice</li>
        <li><svg width="14" height="14" viewBox="0 0 14 14"><circle cx="7" cy="7" r="6" fill="#33a6d7"/><path d="M4 7.2l2 2 4-4" stroke="#fff" stroke-width="1.6" fill="none"/></svg>Succession Planning</li>
      </ul>
    </div>
    <div class="practice-box estate">
      <h2>ESTATE PLANNING</h2>
      <ul>
        <li><svg width="14" height="14" viewBox="0 0 14 14"><circle cx="7" cy="7" r="6" fill="#33a6d7"/><path d="M4 7.2l2 2 4-4" stroke="#fff" stroke-width="1.6" fill="none"/></svg>Wealth strategies to maximise wealth transfer to beneficiaries</li>
        <li><svg width="14" height="14" viewBox="0 0 14 14"><circle cx="7" cy="7" r="6" fill="#33a6d7"/><path d="M4 7.2l2 2 4-4" stroke="#fff" stroke-width="1.6" fill="none"/></svg>Minimise taxes and avoid the probate process</li>
        <li><svg width="14" height="14" viewBox="0 0 14 14"><circle cx="7" cy="7" r="6" fill="#33a6d7"/><path d="M4 7.2l2 2 4-4" stroke="#fff" stroke-width="1.6" fill="none"/></svg>Revocable and irrevocable trusts most suitable for specific situations</li>
        <li><svg width="14" height="14" viewBox="0 0 14 14"><circle cx="7" cy="7" r="6" fill="#33a6d7"/><path d="M4 7.2l2 2 4-4" stroke="#fff" stroke-width="1.6" fill="none"/></svg>Family trusts and bypass trusts</li>
        <li><svg width="14" height="14" viewBox="0 0 14 14"><circle cx="7" cy="7" r="6" fill="#33a6d7"/><path d="M4 7.2l2 2 4-4" stroke="#fff" stroke-width="1.6" fill="none"/></svg>Wills for all estates, simple will and power of attorney</li>
      </ul>
    </div>
  </div>

  <div class="band-intro">
    <h2>BRINDELL LEGAL</h2>
    <p>Personal legal service for Hamilton and the Western District. We combine local knowledge with careful, practical advice across property, business, estates and succession planning.</p>
  </div>
</section>

<section class="team">
  <h2>Our staff that make our boutique the excellent firm it is</h2>
  <div class="team-grid">
    <figure class="team-member"><div class="portrait" role="img" aria-label="Portrait of the principal solicitor"></div><figcaption class="name">Principal Solicitor</figcaption></figure>
    <figure class="team-member"><div class="portrait" role="img" aria-label="Portrait of a staff member in the library"></div><figcaption class="name">Conveyancing Clerk</figcaption></figure>
    <figure class="team-member"><div class="portrait" role="img" aria-label="Portrait of a staff member at the office"></div><figcaption class="name">Legal Assistant</figcaption></figure>
    <figure class="team-member"><div class="portrait" role="img" aria-label="Portrait of a staff member"></div><figcaption class="name">Office Manager</figcaption></figure>
  </div>
</section>

<footer class="site-footer">
  <nav class="footer-nav">
    <a href="#">Home</a><a href="#">About Us</a><a href="#">Leases</a><a href="#">Estate Planning</a><a href="#">Real Estate</a><a href="#">Legal Services</a><a href="#">Your Contact</a>
  </nav>
  <div class="social" aria-label="Social links"><span></span><span></span><span></span><span></span></div>
  <address class="contact" style="font-style:normal">
    17 Pellow Road, Hamilton VIC 3300<br>
    Phone (03) 5598 4731 &nbsp;·&nbsp; Fax (03) 5598 4706<br>
    ross.kedwick@brindelllegal-example.com.au
  </address>
  <div class="footer-rule"></div>
  <p class="copyright">© Copyright Brindell Legal. All rights reserved.</p>
</footer>

</body>
</html>
```